依頼詳細
ロゴはミナモワークスで作成していただいていますので、それを使用していただいきたいです。ホームページは現在作成中です。ロゴを取り入れ、柔らかい雰囲気でシンプルなイメージ、わかりやすい感じがいいです。
記載項目
病院名、ロゴ、開業日、内覧会の日程、住所、電話番号、ホームページのアドレス、診察時間、休診日 対象動物、挨拶等
サイズ
A4
ページ数
片面
希望イメージ
シンプル 複雑
単色 カラフル
暗い 明るい
日常 高級
遊び心 厳粛
未来的 伝統的
女性的 男性的
希望する色
納品ファイル
補足説明
ロゴを添付します。

挨拶内容
「はじめまして、はるかぜペットクリニック院長の森岡健司です。大学卒業後、熊本市内の動物病院で7年間勤務し、2014年3月24日に動物病院を開院することになりました。
ホームドクターとして地域の皆様に親しまれる病院であるとともに、飼い主様と一緒に家族である動物たちの最善のケアができるように努めてまいりたいと思います。ワンちゃん達が遊べるスペースも少しですが用意してあります。ぜひ気軽に遊びにいらしてください。今後ともよろしくお願い致します。」
おそくなりましたが、ホームページのドメイン決まりました。
http://harukaze-petclinic.exampleです。
よろしくお願いいたします。
■ 選んだ理由

シンプルで開院ということがわかりやすかったため。
犬の写真の雰囲気も良かったです。

■ 提案者全員のお礼・コメント

いいデザインを多数いただいてありがとうございます。それぞれおもしろくけっこう悩ませていただきました。また、よろしくお願いいたします。

```html
<!DOCTYPE html>
<html lang="ja">
<head>
<meta charset="utf-8">
<title>はるかぜペットクリニック 開院のお知らせ</title>
<link href="https://fonts.googleapis.com/css2?family=M+PLUS+Rounded+1c:wght@400;500;700;800&display=swap" rel="stylesheet">
<style>
  :root{
    --teal:#2a9bb3;
    --teal-dark:#23708a;
    --teal-pale:#e4f3f6;
    --orange:#ef8328;
    --text:#4a4a4a;
    --line:#bfdfe6;
    --photo-a:#b5763f;
    --photo-b:#d9b48a;
    --map:#eef1f2;
  }
  *{margin:0;padding:0;box-sizing:border-box}
  html,body{width:849px;height:1200px;overflow:hidden;background:#fff}
  body{font-family:"M PLUS Rounded 1c",sans-serif;color:var(--text)}
  .flyer{position:relative;width:849px;height:1200px;background:#fff;overflow:hidden}

  .brand{position:absolute;left:40px;top:26px;display:flex;align-items:center;gap:18px}
  .brand-mark{width:92px;height:92px;border-radius:50%;background:var(--teal);flex:none}
  .brand-en{font-size:22px;font-weight:500;color:var(--teal);letter-spacing:1px}
  .brand-ja{font-size:55px;font-weight:800;color:var(--teal);line-height:1.1}

  .hero-photo{position:absolute;left:0;top:150px;width:600px;height:330px;
    background:linear-gradient(180deg,var(--photo-a) 0%,var(--photo-b) 55%,#fff 100%)}
  .hero-fade{position:absolute;left:0;top:150px;width:600px;height:330px;
    background:linear-gradient(90deg,rgba(255,255,255,0) 70%,#fff 100%)}

  .opening{position:absolute;left:540px;top:190px;width:290px;text-align:center;color:var(--orange)}
  .opening-date{font-size:72px;font-weight:700;line-height:1}
  .opening-date .dow{display:inline-block;font-size:28px;background:var(--orange);color:#fff;
    border-radius:50%;width:44px;height:44px;line-height:44px;vertical-align:middle;margin-left:4px}
  .opening-word{font-size:140px;font-weight:800;line-height:1.15;letter-spacing:-4px}

  .preview{position:absolute;left:30px;top:330px;width:420px;text-align:center}
  .preview-title{font-size:42px;font-weight:800;color:var(--teal-dark);letter-spacing:1px}
  .preview-date{font-size:22px;font-weight:700;color:var(--teal-dark);margin-top:6px}
  .preview-note{font-size:15px;color:var(--orange);margin-top:6px;font-weight:500;white-space:nowrap}

  .cat-illust{position:absolute;left:462px;top:380px;width:70px;height:82px;border-radius:35px 35px 10px 10px;background:#5b4a42}

  .map{position:absolute;left:425px;top:478px;width:395px;height:230px;background:var(--map);
    border:2px solid var(--line);border-radius:6px}

  .greeting{position:absolute;left:30px;top:540px;width:370px}
  .greeting-label{display:inline-block;background:var(--teal);color:#fff;font-weight:700;font-size:20px;
    padding:4px 22px;border-radius:16px 16px 0 0}
  .greeting-body{border-top:3px solid var(--teal);padding-top:10px;font-size:12.5px;line-height:1.7}

  .hours{position:absolute;left:425px;top:730px;width:395px}
  .hours-targets{font-size:13px;color:var(--teal-dark);font-weight:500;margin-bottom:8px}
  .hours-table{width:100%;border-collapse:collapse;font-size:13px;text-align:center}
  .hours-table th,.hours-table td{border:1px solid var(--line);padding:6px 0}
  .hours-table thead th{background:var(--teal);color:#fff;font-weight:500}
  .hours-table tbody th{background:var(--teal-pale);font-weight:500;width:32%}
  .open{color:var(--teal)} .closed{color:var(--orange)}
  .hours-note{text-align:right;font-size:12px;margin-top:6px;color:var(--orange)}

  .footer{position:absolute;left:0;top:995px;width:849px;height:205px;background:var(--teal-pale);border-top:3px solid var(--teal)}
  .footer-brand{position:absolute;left:36px;top:22px;display:flex;align-items:center;gap:14px}
  .footer-mark{width:64px;height:64px;border-radius:50%;background:var(--teal);flex:none}
  .footer-name{font-size:38px;font-weight:800;color:var(--teal)}
  .footer-address{position:absolute;left:116px;top:108px;font-size:18px}
  .footer-url{position:absolute;left:116px;top:140px;font-size:17px;color:var(--teal-dark)}
  .contact{position:absolute;right:32px;top:98px;text-align:right}
  .contact-tel{display:flex;align-items:center;justify-content:flex-end;gap:10px;font-size:42px;font-weight:800;color:var(--orange);line-height:1.1}
  .contact-note{font-size:14px;margin-top:6px}
</style>
</head>
<body>
<main class="flyer">
  <header class="brand">
    <span class="brand-mark"></span>
    <div>
      <p class="brand-en">Harukaze Pet Clinic</p>
      <h1 class="brand-ja">はるかぜペットクリニック</h1>
    </div>
  </header>

  <div class="hero-photo" role="img" aria-label="寄り添う茶色の長毛犬と小型犬の写真"></div>
  <div class="hero-fade"></div>

  <section class="opening">
    <p class="opening-date">3/24<span class="dow">月</span></p>
    <p class="opening-word">開院</p>
  </section>

  <section class="preview">
    <h2 class="preview-title">内覧会のご案内</h2>
    <p class="preview-date">3/21(金)・22(土) 10時～17時予定</p>
    <p class="preview-note">院内をご案内いたしますので、お気軽にお越し下さい。</p>
  </section>

  <div class="cat-illust" role="img" aria-label="座っている猫のシルエットイラスト"></div>

  <div class="map" role="img" aria-label="クリニック周辺の道路と目印を示した案内地図"></div>

  <section class="greeting">
    <h3 class="greeting-label">ご挨拶</h3>
    <p class="greeting-body">はじめまして、はるかぜペットクリニック院長の森岡健司です。大学卒業後、熊本市内の動物病院で7年間勤務し、2014年3月24日に動物病院を開院することになりました。ホームドクターとして地域の皆様に親しまれる病院であるとともに、飼い主様と一緒に家族である動物たちの最善のケアができるように努めてまいりたいと思います。ワンちゃん達が遊べるスペースも少しですが用意してあります。ぜひ気軽に遊びにいらしてください。今後ともよろしくお願い致します。</p>
  </section>

  <section class="hours">
    <p class="hours-targets">犬・猫・うさぎ・ハムスター・その他小動物の診察</p>
    <table class="hours-table">
      <thead><tr><th>診察時間</th><th>月</th><th>火</th><th>水</th><th>木</th><th>金</th><th>土</th><th>日</th></tr></thead>
      <tbody>
        <tr><th>9:00～12:00</th><td class="open">●</td><td class="open">●</td><td class="open">●</td><td class="open">●</td><td class="open">●</td><td class="open">●</td><td class="closed">／</td></tr>
        <tr><th>16:00～19:00</th><td class="open">●</td><td class="open">●</td><td class="open">●</td><td class="open">●</td><td class="open">●</td><td class="open">●</td><td class="closed">／</td></tr>
      </tbody>
    </table>
    <p class="hours-note">休診日：日曜・祝日</p>
  </section>

  <footer class="footer">
    <div class="footer-brand">
      <span class="footer-mark"></span>
      <p class="footer-name">はるかぜペットクリニック</p>
    </div>
    <p class="footer-address">熊本市東区みどり町4丁目11-126</p>
    <p class="footer-url">http://harukaze-petclinic.example</p>
    <div class="contact">
      <p class="contact-tel">
        <svg width="36" height="36" viewBox="0 0 24 24" aria-hidden="true"><path fill="#ef8328" d="M6.6 10.8a15 15 0 0 0 6.6 6.6l2.2-2.2a1 1 0 0 1 1-.25 11.4 11.4 0 0 0 3.6.57 1 1 0 0 1 1 1V20a1 1 0 0 1-1 1A17 17 0 0 1 3 4a1 1 0 0 1 1-1h3.5a1 1 0 0 1 1 1c0 1.25.2 2.46.57 3.6a1 1 0 0 1-.25 1z"/></svg>
        096-555-0142
      </p>
      <p class="contact-note">お気軽にお問い合わせください</p>
    </div>
  </footer>
</main>
</body>
</html>
```